Business Card Design

Name: Dorian Halvik
Title : Mathematics Instructor
Dep. Department of Mathmatics

Four Lindale Court
Westmere, California 94555-0166

T: 805-555-0142
Cell: 805-555-0179

Email: dorian.halvik033@pelmarcu.edu
Email: quickhalvik@zentomail.com

Reason: I don't know how to post my image on the web.

Reason: The design PDF can not be uplorded

Industry/Entity Type

Business

Requirements
Must have
• http://www.pelmarcu.edu/tc/web/styleguide/logos-images.htm

http://www.bentwoodpress.com/pelmarcu/bc/
Nice to have
• I have to use the logo and the format based on their format to some extent.
White back ground

But is there any way to make mine special?
raised ink or 3D logo?

```html
<!DOCTYPE html>
<html lang="en">
<head>
<meta charset="utf-8">
<title>Dorian Halvik – Business Card</title>
<link rel="stylesheet" href="https://fonts.googleapis.com/css2?family=Arimo:ital@0;1&family=Tinos&display=swap">
<style>
  :root {
    --page: #ffffff;
    --frame-red: #d2232a;
    --card-black: #111111;
    --card-edge: #262626;
    --rule-blue: #4a5f9c;
    --text-white: #ffffff;
    --mark-red: #b8232a;
  }
  html, body {
    margin: 0;
    padding: 0;
    width: 1200px;
    height: 702px;
    overflow: hidden;
    background: var(--page);
  }
  .canvas {
    position: relative;
    width: 1200px;
    height: 702px;
    background: var(--page);
  }
  .outer-frame {
    position: absolute;
    left: 22px; top: 20px;
    width: 1150px; height: 649px;
    border: 4px solid var(--frame-red);
  }
  .card {
    position: absolute;
    left: 44px; top: 42px;
    width: 1113px; height: 613px;
    background: radial-gradient(ellipse at 35% 25%, var(--card-edge) 0%, var(--card-black) 70%);
    overflow: hidden;
  }
  .card-swooshes {
    position: absolute;
    inset: 0;
  }
  .brand-seal {
    position: absolute;
    left: 42px; top: 21px;
    width: 166px; height: 166px;
    border-radius: 50%;
    background: var(--page);
    border: 5px solid var(--frame-red);
    display: flex;
    align-items: center;
    justify-content: center;
  }
  .brand-name {
    font-family: "Tinos", serif;
    font-size: 30px;
    color: var(--mark-red);
  }
  .person-name {
    position: absolute;
    right: 37px; top: 205px;
    margin: 0;
    font-family: "Tinos", serif;
    font-weight: 400;
    font-size: 80px;
    line-height: 1;
    letter-spacing: 1px;
    color: var(--text-white);
    white-space: nowrap;
  }
  .name-rule {
    position: absolute;
    left: 274px; top: 289px;
    width: 821px; height: 2px;
    background: var(--rule-blue);
  }
  .job-title {
    position: absolute;
    left: 565px; top: 296px;
    font-family: "Arimo", sans-serif;
    font-style: italic;
    font-size: 42px;
    line-height: 1;
    color: var(--text-white);
    white-space: nowrap;
  }
  .department {
    position: absolute;
    left: 605px; top: 341px;
    font-family: "Arimo", sans-serif;
    font-style: italic;
    font-size: 24px;
    line-height: 1;
    color: var(--text-white);
    white-space: nowrap;
  }
  .contact {
    font-family: "Arimo", sans-serif;
    font-size: 31px;
    line-height: 1;
    color: var(--text-white);
  }
  .contact-line,
  .contact-label {
    position: absolute;
    white-space: nowrap;
  }
</style>
</head>
<body>
<div class="canvas">
  <div class="outer-frame"></div>
  <div class="card">
    <svg class="card-swooshes" width="1113" height="613" viewBox="0 0 1113 613" aria-hidden="true">
      <defs>
        <linearGradient id="swooshFade" x1="0" y1="0" x2="1" y2="1">
          <stop offset="0" stop-color="#4a4a4a" stop-opacity="0.55"/>
          <stop offset="1" stop-color="#1a1a1a" stop-opacity="0"/>
        </linearGradient>
      </defs>
      <path d="M0 40 C260 120 520 300 700 613 L620 613 C460 330 230 160 0 100 Z" fill="url(#swooshFade)"/>
      <path d="M120 0 C420 120 700 320 900 613 L840 613 C640 340 380 140 60 0 Z" fill="url(#swooshFade)" opacity="0.7"/>
      <path d="M300 0 C620 90 900 300 1113 560 L1113 613 C880 340 600 110 240 0 Z" fill="url(#swooshFade)" opacity="0.5"/>
      <path d="M0 260 C200 300 380 420 470 613 L430 613 C330 440 170 330 0 310 Z" fill="url(#swooshFade)" opacity="0.6"/>
    </svg>

    <div class="brand-seal"><span class="brand-name">pelmarcu</span></div>

    <h1 class="person-name">Dorian Halvik</h1>
    <div class="name-rule"></div>
    <div class="job-title">Mathematics instructor</div>
    <div class="department">Dep. Department of Mathmatics</div>

    <div class="contact">
      <span class="contact-label" style="left:28px; top:397px;">Address</span>
      <span class="contact-line" style="left:171px; top:397px;">:Four Lindale Court</span>
      <span class="contact-line" style="left:179px; top:433px;">Westmere, California 94555-0166</span>
      <span class="contact-label" style="left:31px; top:470px;">Email</span>
      <span class="contact-line" style="left:169px; top:470px;">:dorian.halvik033@pelmarcu.edu</span>
      <span class="contact-label" style="left:31px; top:508px;">Email</span>
      <span class="contact-line" style="left:169px; top:508px;">:quickhalvik@zentomail.com</span>
      <span class="contact-line" style="left:226px; top:550px;">Tel : 805-555-0142</span>
      <span class="contact-label" style="left:638px; top:550px;">Mobile:</span>
      <span class="contact-line" style="left:779px; top:554px;">805-555-0179</span>
    </div>
  </div>
</div>
</body>
</html>
```